Banner ad to encourage people to complete a survey

This is a banner ad which will be posted on www.veltrona.org. The goal of the add is to encourage people to click on it and take the survey.
File Format: Standard .jpg image (no Flash)
Ad dimension (Pixels): 300w x 250d
Max File Size: 24k
- Use a border to differentiate the banner from page content (page background is white)
- No transparent backgrounds
Ad Message: "Speech-Language Pathologist Survey"
Additional text: "Please take two minutes to complete a survey on the future of work patterns for Speech-Language Pathologists and enter a draw to win an Zorbik"
Target Market(s)
The respondents are professional and well educated and the ad/colour scheme should reflect this.
Font styles to use
Colors
Designer to choose colors to be used in the design.
Look and feel

```html
<!DOCTYPE html>
<html lang="en">
<head>
<meta charset="utf-8">
<title>Static Banner Preview</title>
<link href="https://fonts.googleapis.com/css2?family=Arimo:ital,wght@0,400;0,700;1,700&display=swap" rel="stylesheet">
<style>
  :root {
    --band-dark: #2e4a2a;
    --band-light: #7a9c5f;
    --sheet: #fcfcfc;
    --title-grey: #c2c2c2;
    --ink: #3a3a3a;
    --white: #ffffff;
    --accent-green: #5cb040;
    --button-green: #4e9a35;
    --button-edge: #3c7d27;
    --badge-orange: #f39a1c;
    --badge-ink: #111111;
  }
  * { margin: 0; padding: 0; box-sizing: border-box; }
  html, body { width: 1200px; height: 1200px; overflow: hidden; }
  body { font-family: "Arimo", Arial, sans-serif; position: relative; background: var(--sheet); }

  .header-band { position: absolute; left: 0; top: 0; width: 1200px; height: 362px; background: var(--band-dark); }
  .preview-title {
    position: absolute; left: 100px; top: 38px;
    color: var(--title-grey); font-weight: 400; font-size: 100px; line-height: 87px; letter-spacing: 1px;
  }
  .preview-note {
    position: absolute; left: 101px; top: 306px;
    color: var(--title-grey); font-size: 34px; line-height: 40px;
  }

  .sheet-band { position: absolute; left: 0; top: 362px; width: 1200px; height: 510px; background: var(--sheet); }

  .banner {
    position: absolute; left: 102px; top: 416px; width: 480px; height: 400px; overflow: hidden;
    color: var(--white);
  }
  .banner-scene {
    position: absolute; inset: 0;
    background:
      radial-gradient(ellipse 60% 40% at 60% 78%, rgba(140,150,160,0.55), transparent 70%),
      linear-gradient(180deg, #3b4a3a 0%, #556354 38%, #3a4230 62%, #2a2a24 100%);
  }
  .banner-headline {
    position: absolute; left: 27px; top: 14px; width: 440px;
    font-weight: 700; font-size: 35px; line-height: 42px; color: #eef0f4;
    text-shadow: 0 2px 4px rgba(0,0,0,0.6);
  }
  .banner-copy {
    position: absolute; left: 20px; top: 184px; width: 300px;
    font-weight: 700; font-style: italic; font-size: 24px; line-height: 29px;
    text-shadow: 0 1px 3px rgba(0,0,0,0.7);
  }
  .banner-copy .highlight { color: var(--accent-green); }
  .survey-button {
    position: absolute; left: 18px; top: 318px; width: 211px; height: 61px;
    background: linear-gradient(180deg, #62b048, var(--button-green));
    border: 2px solid var(--button-edge); border-radius: 6px;
    display: flex; align-items: center; justify-content: center; gap: 12px;
    font-size: 29px; color: var(--white);
  }
  .survey-button svg { width: 14px; height: 22px; }
  .prize-badge {
    position: absolute; left: 262px; top: 232px; width: 300px; height: 300px; border-radius: 50%;
    background: var(--badge-orange); border: 12px solid var(--white);
  }
  .prize-text {
    position: absolute; left: 292px; top: 254px; width: 210px; text-align: center; font-weight: 700;
  }
  .prize-enter { color: var(--white); font-size: 26px; line-height: 28px; }
  .prize-win { color: var(--badge-ink); font-size: 35px; line-height: 40px; font-style: italic; }
  .prize-name { color: var(--badge-ink); font-size: 54px; line-height: 58px; }

  .demo-info { position: absolute; left: 618px; top: 416px; color: var(--ink); }
  .demo-name { font-size: 48px; font-weight: 700; line-height: 56px; }
  .demo-size { font-size: 48px; line-height: 56px; }
  .demo-brief { font-size: 32px; line-height: 40px; }

  .footer-band { position: absolute; left: 0; top: 872px; width: 1200px; height: 328px; background: var(--band-light); }
  .footer-note { position: absolute; left: 101px; top: 227px; color: var(--white); font-size: 34px; line-height: 40px; }
</style>
</head>
<body>
  <header class="header-band">
    <h1 class="preview-title">STATIC<br>BANNER<br>PREVIEW</h1>
    <p class="preview-note">To be supplied as original Pixelmont file (PSD uncoded) layout only</p>
  </header>

  <section class="sheet-band"></section>

  <div class="banner">
    <div class="banner-scene" role="img" aria-label="Photo of a wet road winding through a misty autumn forest"></div>
    <p class="banner-headline">Communication fears shouldn't be a lonely road to nowhere</p>
    <p class="banner-copy">Please help <span class="highlight">determine the future</span> of work patterns for Speech-Language Pathologists</p>
    <div class="survey-button">Take Survey
      <svg viewBox="0 0 14 22"><path d="M2 2 L11 11 L2 20" fill="none" stroke="#fff" stroke-width="3.5"/></svg>
    </div>
    <div class="prize-badge"></div>
    <div class="prize-text">
      <p class="prize-enter">ENTER<br>THE DRAW</p>
      <p class="prize-win">to win an</p>
      <p class="prize-name">Zorbik</p>
    </div>
  </div>

  <div class="demo-info">
    <p class="demo-name">DEMO 1</p>
    <p class="demo-size">Size: 300w x 250h</p>
    <p class="demo-brief">As per design brief</p>
  </div>

  <footer class="footer-band">
    <p class="footer-note">(other sizes can be made)</p>
  </footer>
</body>
</html>
```